Tall Gum Equipment Hire Business Card Design

Tall Gum Equipment Hire Pty Ltd

WET or DRY HIRE

Kestro T5-8 + attachments
Turf Cutter
Lawn mowers with catchers
Brushcutters
Blowers

We require a business card with the above information for a new equipment hire Company. Would like to see a redish/brown background or something to do with an Australian Red Dog (Cattle Dog) on the business card as our Logo - even some sort of watermark as a background.

Business

ABN: 71 382 915 206
17C Hollins Road Emerald Qld 4720
PO Box 5817 Emerald Qld 4720
PH: 0417362908 or 0438105724
Email: fastslash@coralnetmail.com

```html
<!DOCTYPE html>
<html lang="en">
<head>
<meta charset="utf-8">
<title>Tall Gum Equipment Hire Pty Ltd – Business Card</title>
<link rel="stylesheet" href="https://fonts.googleapis.com/css2?family=Quicksand:wght@400;500&display=swap">
<style>
  :root {
    --backdrop: #2a1414;
    --card-top: #9c2a1e;
    --card-mid: #7d2219;
    --card-bottom: #5a1813;
    --ink: #f1d98c;
    --ink-soft: rgba(241, 217, 140, 0.9);
  }
  * { box-sizing: border-box; margin: 0; padding: 0; }
  html, body {
    width: 1200px;
    height: 800px;
    overflow: hidden;
    background: var(--backdrop);
  }
  .stage {
    width: 1200px;
    height: 800px;
    display: flex;
    align-items: center;
    justify-content: center;
  }
  .business-card {
    position: relative;
    width: 900px;
    height: 514px;
    background: linear-gradient(170deg, var(--card-top) 0%, var(--card-mid) 45%, var(--card-bottom) 100%);
    font-family: "Quicksand", "Trebuchet MS", sans-serif;
    color: var(--ink);
    box-shadow: 0 18px 40px rgba(0, 0, 0, 0.45);
  }
  .brand {
    position: absolute;
    left: 230px;
    top: 96px;
    width: 560px;
    font-weight: 500;
    font-size: 46px;
    line-height: 1.1;
    letter-spacing: 0.5px;
    color: var(--ink);
  }
  .contact-list {
    position: absolute;
    left: 150px;
    top: 300px;
    list-style: none;
    font-weight: 400;
    font-size: 19px;
    line-height: 27px;
    color: var(--ink-soft);
  }
  .contact-item {
    display: flex;
    align-items: center;
    gap: 10px;
  }
  .contact-icon {
    width: 20px;
    height: 18px;
    flex: none;
    fill: var(--ink);
  }
  .contact-item--plain { padding-left: 30px; }
</style>
</head>
<body>
<main class="stage">
  <article class="business-card">
    <h1 class="brand">Tall Gum Equipment Hire Pty Ltd</h1>

    <ul class="contact-list">
      <li class="contact-item">
        <svg class="contact-icon" viewBox="0 0 20 18" aria-hidden="true"><path d="M10 1 1 9h3v8h5v-5h2v5h5V9h3z"/></svg>
        17C Hollins Road Emerald Qld 4720
      </li>
      <li class="contact-item">
        <svg class="contact-icon" viewBox="0 0 20 18" aria-hidden="true"><path d="M10 1 1 9h3v8h5v-5h2v5h5V9h3z"/></svg>
        PO Box 5817 Emerald Qld 4720
      </li>
      <li class="contact-item">
        <svg class="contact-icon" viewBox="0 0 20 18" aria-hidden="true"><path d="M5 1c1 0 2 3 2 4s-2 1-2 2c0 2 4 6 6 6 1 0 1-2 2-2s4 1 4 2-2 4-4 4C8 17 2 11 2 5c0-2 2-4 3-4z"/></svg>
        0417362908
      </li>
      <li class="contact-item">
        <svg class="contact-icon" viewBox="0 0 20 18" aria-hidden="true"><path d="M5 1c1 0 2 3 2 4s-2 1-2 2c0 2 4 6 6 6 1 0 1-2 2-2s4 1 4 2-2 4-4 4C8 17 2 11 2 5c0-2 2-4 3-4z"/></svg>
        0438105724
      </li>
      <li class="contact-item">
        <svg class="contact-icon" viewBox="0 0 20 18" aria-hidden="true"><path d="M1 3h18v12H1zM2 4l8 6 8-6v1l-8 6-8-6z" fill-rule="evenodd"/></svg>
        fastslash@coralnetmail.com
      </li>
      <li class="contact-item contact-item--plain">ABN: 71 382 915 206</li>
    </ul>
  </article>
</main>
</body>
</html>
```